Safety Brochure for Industry Assocations

This is an 8.5 x 11 single sided brochure for our Occupational Health and Safety Data Analytics software. If you need to use stock images we will pay for them.

Please incorporate our logo and some of the images. No need to incorporate them all. We like the idea of the boots being at the bottom of the page but we're open to other ideas.

Please note that we intend to mail this brochure to different industries so it should be generic (i.e. not construction specific).

Target Market(s)

Safety and Industry Organisations for construction, mining, forestry and oil and gas industries.

Industry/Entity Type

Industry

Font styles to use
Sans Serif

Colors

Designer to choose colors to be used in the design.

Requirements
Must have
• We are a software company that produces safety software. Our customers are companies that engage in dangerous work and use our software to improve their worker's safety. The look and feel should convey the fact that:
• -We are Big Data
• -We are Software
• -We service industry
Nice to have
• Please see the Pixfold photo of the boots. We were hoping that the desiger would be able ti modify the image with an overlay of 0's and 1's in a kind of "matrix" fashion to indicate that we are merging traditional labour work with software.
Should not have
• No medical symbols. Note that WE ARE NOT HEALTH CARE.

```html
<!DOCTYPE html>
<html lang="en">
<head>
<meta charset="utf-8">
<title>Stratum Analytics – Safety Brochure</title>
<link href="https://fonts.googleapis.com/css2?family=Open+Sans:wght@400;600;700&family=Quicksand:wght@400;500;600&display=swap" rel="stylesheet">
<style>
  :root {
    --green: #3cb04a;
    --green-dark: #17a34a;
    --green-lime: #9ccc3c;
    --charcoal: #444142;
    --text: #5a5a5a;
    --paper: #f1f1f1;
    --white: #ffffff;
  }
  * { margin: 0; padding: 0; box-sizing: border-box; }
  html, body { width: 958px; height: 1200px; overflow: hidden; background: #e9e9e9; }
  .brochure {
    position: relative; width: 958px; height: 1200px; overflow: hidden;
    background: repeating-linear-gradient(-60deg, #f4f4f4 0 6px, #eeeeee 6px 8px);
    font-family: "Open Sans", sans-serif; color: var(--text);
  }
  .top-bar { position: absolute; left: 0; top: 0; width: 100%; height: 13px; background: var(--green); }
  .hero-photo {
    position: absolute; left: 0; top: 13px; width: 100%; height: 485px;
    background:
      radial-gradient(ellipse 45% 40% at 50% 58%, #6b4a2c 0%, #8a6543 45%, rgba(138,101,67,0) 75%),
      linear-gradient(180deg, #f3f3f3 0%, #e6e6e6 70%, #b9b2a8 82%, #8c857c 100%);
  }
  .headline-band {
    position: absolute; left: 0; top: 498px; width: 100%; height: 118px;
    background: var(--charcoal); color: var(--white); text-align: center;
  }
  .headline-band h1 { font-weight: 400; font-size: 35px; margin-top: 14px; letter-spacing: 0.2px; }
  .headline-band h1 strong { font-weight: 700; }
  .headline-band p { font-size: 29px; margin-top: 6px; }
  .band-notch {
    position: absolute; left: 474px; top: 615px; width: 0; height: 0;
    border-left: 16px solid transparent; border-right: 16px solid transparent;
    border-top: 14px solid var(--charcoal);
  }
  .pitch { position: absolute; left: 30px; top: 650px; width: 420px; }
  .pitch h2 { color: var(--green); font-size: 30px; font-weight: 700; line-height: 39px; }
  .pitch ul { list-style: none; margin-top: 26px; font-family: "Quicksand", sans-serif; font-size: 20.5px; line-height: 35px; font-weight: 500; }
  .pitch ul b { font-family: "Open Sans", sans-serif; color: var(--green); font-weight: 600; }
  .brand { position: absolute; left: 30px; top: 1060px; display: flex; align-items: center; gap: 16px; }
  .brand-dot { width: 56px; height: 56px; border-radius: 50%; background: var(--green); }
  .brand-name { font-family: "Quicksand", sans-serif; font-weight: 600; font-size: 30px; color: var(--charcoal); letter-spacing: 2px; }
  .data-panel h2 { position: absolute; left: 473px; top: 652px; color: var(--charcoal); font-size: 31px; font-weight: 700; }
  .data-rule { position: absolute; left: 473px; top: 695px; width: 110px; border-top: 1px dashed #aaa; }
  .data-spine { position: absolute; left: 473px; top: 695px; height: 335px; border-left: 1px dashed #aaa; }
  .data-item { position: absolute; left: 486px; width: 460px; height: 115px; }
  .data-item svg { position: absolute; left: 0; top: 0; }
  .data-item .connector { position: absolute; left: 114px; top: 57px; width: 40px; border-top: 2px dashed var(--green); }
  .data-item .copy { position: absolute; left: 160px; top: 18px; font-size: 13.5px; line-height: 22px; color: var(--charcoal); }
  .data-item .copy h3 { color: var(--green); font-size: 16px; font-weight: 600; line-height: 22px; }
  .contact-card {
    position: absolute; left: 473px; top: 1073px; width: 473px; height: 104px;
    background: var(--charcoal); border-radius: 10px; color: var(--white);
    padding: 10px 0 0 26px; z-index: 2;
  }
  .contact-card p { font-size: 20px; line-height: 30px; }
  .contact-card strong { display: block; font-size: 20px; font-weight: 700; line-height: 28px; letter-spacing: 0.5px; }
  .bottom-bar { position: absolute; left: 0; bottom: 0; width: 100%; height: 42px; background: var(--green); }
</style>
</head>
<body>
<main class="brochure">
  <div class="top-bar"></div>
  <div class="hero-photo" role="img" aria-label="Photo of a pair of worn leather work boots on a wooden floor against a white brick wall"></div>

  <header class="headline-band">
    <h1>The next <strong>BIG STEP</strong> in injury reduction!</h1>
    <p>For your entire industry!</p>
  </header>
  <div class="band-notch"></div>

  <section class="pitch">
    <h2>Leverage the power<br>of BIG DATA!</h2>
    <ul>
      <li><b>LEAD</b> the next wave of injury reduction</li>
      <li><b>ENGAGE</b> with members through collaboration and benchmarking</li>
      <li><b>PROMOTE</b> standardization</li>
      <li><b>ANALYZE</b> Accurate, Timely and Complete Leading Indicators</li>
      <li><b>TRAIN</b> industry more proactively</li>
    </ul>
  </section>

  <div class="brand">
    <span class="brand-dot"></span>
    <span class="brand-name">Stratum Analytics</span>
  </div>

  <section class="data-panel">
    <h2>EHS Data</h2>
    <div class="data-rule"></div>
    <div class="data-spine"></div>

    <div class="data-item" style="top:710px">
      <svg width="115" height="115" viewBox="0 0 115 115">
        <circle cx="57" cy="57" r="50" fill="none" stroke="#ddd" stroke-width="10"/>
        <path d="M57 7 A50 50 0 1 0 107 57" fill="none" stroke="var(--green-dark)" stroke-width="10"/>
        <circle cx="57" cy="57" r="38" fill="#fff"/>
        <circle cx="57" cy="53" r="9" fill="var(--green-dark)"/>
        <rect x="53" y="61" width="8" height="7" rx="1" fill="var(--green-dark)"/>
      </svg>
      <div class="connector"></div>
      <div class="copy"><h3>Training</h3>Analyze needs of Industry<br>Deliver Proactive Training<br>Improve Safety</div>
    </div>

    <div class="data-item" style="top:818px">
      <svg width="115" height="115" viewBox="0 0 115 115">
        <circle cx="57" cy="57" r="50" fill="none" stroke="#ddd" stroke-width="10"/>
        <path d="M57 7 A50 50 0 0 1 57 107" fill="none" stroke="var(--green)" stroke-width="10"/>
        <circle cx="57" cy="57" r="38" fill="#fff"/>
        <rect x="38" y="41" width="38" height="28" fill="none" stroke="var(--green)" stroke-width="2"/>
        <polyline points="42,60 50,52 58,56 72,45" fill="none" stroke="var(--green)" stroke-width="2"/>
        <rect x="60" y="58" width="3" height="9" fill="var(--green)"/>
        <rect x="66" y="54" width="3" height="13" fill="var(--green)"/>
      </svg>
      <div class="connector"></div>
      <div class="copy"><h3>Benchmarking</h3>Engage with Members<br>Promote Collaborative Advancement of Safety<br>Improve Safety</div>
    </div>

    <div class="data-item" style="top:926px">
      <svg width="115" height="115" viewBox="0 0 115 115">
        <circle cx="57" cy="57" r="50" fill="none" stroke="#ddd" stroke-width="10"/>
        <path d="M57 107 A50 50 0 1 1 107 57" fill="none" stroke="var(--green-lime)" stroke-width="10"/>
        <circle cx="57" cy="57" r="38" fill="#fff"/>
        <rect x="44" y="60" width="5" height="9" fill="var(--green-lime)"/>
        <rect x="51" y="55" width="5" height="14" fill="var(--green-lime)"/>
        <rect x="58" y="50" width="5" height="19" fill="var(--green-lime)"/>
        <rect x="65" y="45" width="5" height="24" fill="var(--green-lime)"/>
      </svg>
      <div class="connector"></div>
      <div class="copy"><h3>Trend Analysis</h3>Monitor Industry Trends<br>Implement Corrective Initiatives<br>Improve Safety</div>
    </div>
  </section>

  <aside class="contact-card">
    <p>For more information please contact us:</p>
    <strong>1-888-555-0142</strong>
    <strong>www.stratumanalytics.com</strong>
  </aside>

  <div class="bottom-bar"></div>
</main>
</body>
</html>
```